Brochure and Flyer template, Aluminium Facade company
Verdantis Structural Concepts pty Ltd
We are looking for a cutting edge Brochure and Flyer template that we can change text and pictures for different marketing products and services we provide to different target markets and audiences. We like a mixture of A4 size but also like the A5 size so please feel free to be creative.
Construction
Corporate, Building Companies, Architects, Home owners.
We are needing the Brochure template to cater for multiple product pictures and descriptions in either A4 or A5 format (please be creative) and the flier template is more aimed to focus on 1 or 2 individual products.
1 of 2 files of Past project photos for your use if you like
Our Logo
Our Logo Different Format
Our Company Profile (old and out dated for reference only!)
2 of 2 files of Past project photos for your use if you like
Past Projects for information on our company
SOME of our standard Products FOR YOUR INFORMATION ONLY
Havenor opening roof System Photos to go with the operable section Please make sure the Havenor logo is used
Our Products and Services description
Havenor opening Roof information
More Havenor opening roof pics and data. May be of use

```html
<!DOCTYPE html>
<html lang="en">
<head>
<meta charset="utf-8">
<title>Verdantis Structural Concepts – Product Flyers</title>
<link rel="stylesheet" href="https://fonts.googleapis.com/css2?family=Archivo:wght@400;700&family=Arimo:wght@400;700&display=swap">
<style>
  :root {
    --backdrop: #858585;
    --paper: #ffffff;
    --ink: #1c1c1c;
    --body-ink: #2e2e2e;
    --green: #2f9a57;
    --footer: #4a4a4a;
    --footer-ink: #e8e8e8;
    --photo-sky: #b9c9d6;
    --photo-deck: #8c7f6e;
    --photo-timber: #5a3d2c;
  }
  * { box-sizing: border-box; margin: 0; padding: 0; }
  html, body { width: 1200px; height: 850px; overflow: hidden; }
  body {
    background: radial-gradient(ellipse at center, #9a9a9a 0%, var(--backdrop) 70%);
    font-family: "Arimo", Arial, sans-serif;
    position: relative;
  }
  .page {
    position: absolute;
    top: 29px;
    width: 570px;
    height: 795px;
    background: var(--paper);
    box-shadow: 0 4px 14px rgba(0,0,0,.35);
    overflow: hidden;
  }
  .page--brochure { left: 19px; }
  .page--flyer { left: 612px; }
  .page-title {
    position: absolute;
    left: 34px;
    top: 76px;
    font-family: "Archivo", Arial, sans-serif;
    font-weight: 700;
    font-size: 22px;
    letter-spacing: 1.8px;
    color: var(--ink);
  }
  .rule {
    position: absolute;
    left: 34px;
    right: 24px;
    top: 112px;
    height: 4px;
    background: var(--green);
  }
  .photo { position: absolute; }
  .product-shot {
    left: 400px; top: 14px; width: 156px; height: 80px;
    background: linear-gradient(160deg, #d9dde0, #9aa2a8 60%, #c6cbcf);
  }
  .gallery {
    position: absolute;
    left: 34px; top: 129px;
    width: 518px; height: 240px;
    display: grid;
    grid-template-columns: repeat(3, 1fr);
    grid-template-rows: repeat(2, 1fr);
    gap: 5px;
  }
  .gallery .tile { background: linear-gradient(180deg, var(--photo-sky), #d6d8d4 45%, var(--photo-deck)); }
  .gallery .tile:nth-child(2), .gallery .tile:nth-child(5) { background: linear-gradient(180deg, #cfd3d2, #7c95a8 55%, #4e6a7c); }
  .gallery .tile:nth-child(3), .gallery .tile:nth-child(6) { background: linear-gradient(180deg, #e4e0d4, #c9b99a 55%, #8fa07c); }
  .copy {
    position: absolute;
    left: 34px;
    width: 512px;
    font-size: 13.4px;
    line-height: 16px;
    color: var(--body-ink);
  }
  .brochure-intro { top: 393px; }
  .brochure-detail { top: 475px; }
  .flyer-intro { top: 160px; }
  .flyer-detail { top: 258px; }
  .quote-mark {
    position: absolute;
    left: 34px; top: 572px;
    font-family: "Archivo", Arial, sans-serif;
    font-weight: 700;
    font-size: 32px;
    color: var(--green);
  }
  .quote {
    position: absolute;
    left: 60px; top: 605px; width: 455px;
    font-size: 13.4px; line-height: 16px;
    color: var(--body-ink);
  }
  .quote-author {
    position: absolute;
    left: 395px; top: 684px;
    font-size: 13px;
    color: var(--green);
  }
  .louvre-shot {
    left: 0; top: 330px; width: 430px; height: 415px;
    background: linear-gradient(135deg, var(--photo-timber) 0%, #7a5a44 45%, #cfc6bd 100%);
  }
  .circle-shot {
    left: 240px; top: 336px; width: 192px; height: 192px;
    border-radius: 50%;
    border: 4px solid var(--paper);
    background: linear-gradient(180deg, #e6e6e4, #b8bfc2 45%, #8a9a86);
  }
  .footer {
    position: absolute;
    left: 0; right: 0; bottom: 0;
    height: 50px;
    background: var(--footer);
    display: flex;
    align-items: center;
    justify-content: space-between;
    padding: 0 22px 0 28px;
  }
  .footer-note { font-size: 12px; color: var(--footer-ink); }
  .brand { display: flex; align-items: center; gap: 7px; }
  .brand-dot { width: 20px; height: 20px; border-radius: 50%; background: var(--footer-ink); }
  .brand-name {
    font-family: "Archivo", Arial, sans-serif;
    font-weight: 700;
    font-size: 17px;
    color: var(--footer-ink);
    letter-spacing: .5px;
  }
</style>
</head>
<body>

<section class="page page--brochure">
  <div class="photo product-shot" role="img" aria-label="Aluminium elliptical blade profiles"></div>
  <h1 class="page-title">ELLIPTICAL BLADES</h1>
  <div class="rule"></div>
  <div class="gallery">
    <div class="tile" role="img" aria-label="Pergola with elliptical roof blades"></div>
    <div class="tile" role="img" aria-label="Covered terrace overlooking harbour"></div>
    <div class="tile" role="img" aria-label="Outdoor living area under blade roof"></div>
    <div class="tile" role="img" aria-label="Open roof blades above a patio"></div>
    <div class="tile" role="img" aria-label="Poolside shade structure"></div>
    <div class="tile" role="img" aria-label="Garden pavilion with louvred roof"></div>
  </div>
  <p class="copy brochure-intro">Lorem ipsum dolor sit amet, consectetur adipiscing elit. Nunc eget sem condimentum arcu elementum fermentum non vitae felis. Quisque convallis vehicula justo sed venenatis. Curabitur vitae odio et neque ornare facilisis ac vel lacus.</p>
  <p class="copy brochure-detail">trum. Cras magna enim, pellentesque non venenatis id, vestibulum a sem. Vestibulum porta tristique felis, quis vulputate sem tempor eu. Ut blandit massa ac dui porttitor cursus. Vivamus nec nisl ac erat scelerisque pretium ut a nunc.</p>
  <div class="quote-mark">“</div>
  <p class="quote">Nulla vehicula a velit id rutrum. Cras magna enim, pellentesque non venenatis id, vestibulum a sem. Vestibulum porta tristique felis, quis vulputate sem tempor eu.</p>
  <p class="quote-author">Mara Lind, QRS</p>
  <footer class="footer">
    <span class="footer-note">© 2013 Verdantis Structural Concepts Pty Ltd</span>
    <span class="brand"><span class="brand-dot"></span><span class="brand-name">VERDANTIS</span></span>
  </footer>
</section>

<section class="page page--flyer">
  <h1 class="page-title">VANTALATION LOUVRE BLADES</h1>
  <div class="rule"></div>
  <p class="copy flyer-intro">Lorem ipsum dolor sit amet, consectetur adipiscing elit. Nunc eget sem condimentum arcu elementum fermentum non vitae felis. Quisque convallis vehicula justo sed venenatis. Curabitur vitae odio et neque ornare facilisis ac vel lacus.</p>
  <p class="copy flyer-detail">trum. Cras magna enim, pellentesque non venenatis id, vestibulum a sem. Vestibulum porta tristique felis, quis vulputate sem tempor eu. Ut blandit massa ac dui porttitor cursus. Vivamus nec nisl ac erat scelerisque pretium ut a nunc.</p>
  <div class="photo louvre-shot" role="img" aria-label="Row of vertical timber-look louvre blades"></div>
  <div class="photo circle-shot" role="img" aria-label="Louvred roof over an outdoor terrace"></div>
  <footer class="footer">
    <span class="footer-note">© 2013 Verdantis Structural Concepts Pty Ltd</span>
    <span class="brand"><span class="brand-dot"></span><span class="brand-name">VERDANTIS</span></span>
  </footer>
</section>

</body>
</html>
```